Van Signage for Tech Company - Small Van and Mid-Size Van

Looking for a simple yet eye-catching van signage. Just Company Logo, Web Address and Phone number. - we like the idea of a digital wave of sorts, something that would compliment our logo design/color.

Our Business Area is

Satellite / TV
Wi-Fi
Smart Home
Communications

It would be great to have icons that would represent each of these areas we work.

Industry/Entity Type

Wireless Communication

Font styles to use
Sans Serif

```html
<!DOCTYPE html>
<html lang="en">
<head>
<meta charset="utf-8">
<title>Zentra Van Side Signage</title>
<link rel="stylesheet" href="https://fonts.googleapis.com/css2?family=PT+Sans+Narrow:wght@400;700&display=swap">
<style>
  :root {
    --backdrop: #5675b3;
    --panel: #ffffff;
    --brand-blue: #2f5ea8;
    --phone-blue: #1030b0;
    --web-rust: #a8360e;
    --tagline-grey: #4a4a55;
    --tone-lime: rgba(200, 224, 74, 0.55);
    --tone-silver: rgba(185, 188, 196, 0.45);
    --tone-pink: rgba(224, 79, 184, 0.45);
    --tone-violet: rgba(154, 123, 224, 0.4);
  }
  * { margin: 0; padding: 0; box-sizing: border-box; }
  html, body {
    width: 1200px;
    height: 900px;
    overflow: hidden;
    background: var(--backdrop);
    font-family: "PT Sans Narrow", sans-serif;
  }
  .canvas {
    position: relative;
    width: 1200px;
    height: 900px;
  }
  .van-side-panel {
    position: absolute;
    left: 100px;
    top: 220px;
    width: 1000px;
    height: 440px;
    background: var(--panel);
    border-radius: 18px;
    overflow: hidden;
    box-shadow: 0 18px 40px rgba(20, 35, 80, 0.35);
  }
  .wave-artwork {
    position: absolute;
    left: 0;
    top: 0;
    width: 1000px;
    height: 300px;
    background:
      linear-gradient(to bottom, rgba(255,255,255,0) 0%, rgba(255,255,255,0) 45%, var(--panel) 100%),
      linear-gradient(to right, var(--tone-lime) 0%, var(--tone-silver) 35%, var(--tone-pink) 62%, var(--tone-violet) 100%);
  }
  .brand-lockup {
    position: absolute;
    right: 60px;
    top: 40px;
    text-align: right;
  }
  .brand-name {
    font-weight: 700;
    font-size: 120px;
    line-height: 1;
    color: var(--brand-blue);
    letter-spacing: 2px;
  }
  .brand-tagline {
    font-weight: 400;
    font-size: 28px;
    color: var(--tagline-grey);
    margin-top: 4px;
  }
  .service-list {
    position: absolute;
    left: 70px;
    top: 190px;
    list-style: none;
  }
  .service-list li {
    font-weight: 700;
    font-size: 32px;
    line-height: 42px;
    color: var(--brand-blue);
  }
  .contact-block {
    position: absolute;
    right: 60px;
    top: 250px;
    text-align: center;
  }
  .contact-phone {
    font-weight: 700;
    font-size: 32px;
    color: var(--phone-blue);
    letter-spacing: 1px;
  }
  .contact-web {
    font-weight: 700;
    font-size: 32px;
    color: var(--web-rust);
    letter-spacing: 2px;
    margin-top: 4px;
  }
</style>
</head>
<body>
<main class="canvas">
  <section class="van-side-panel">
    <div class="wave-artwork" role="img" aria-label="Decorative flowing colour wave artwork in lime, silver, pink and violet tones"></div>

    <header class="brand-lockup">
      <div class="brand-name">Zentra</div>
      <div class="brand-tagline">connected living, made simple</div>
    </header>

    <ul class="service-list">
      <li>Wi-Fi</li>
      <li>Smart Home</li>
      <li>Satellite / TV</li>
      <li>Communications</li>
    </ul>

    <div class="contact-block">
      <div class="contact-phone">00 555 0199</div>
      <div class="contact-web">www.zentralink.com</div>
    </div>
  </section>
</main>
</body>
</html>
```